Verdanix Medical Business Card

Create a high class Business card for Medical Aesthetics and Wellness Practice called Verdanix Medical Aesthetics and Wellness as per the logo attached.
Addresss is: 418 Harlan Brook Road Suite 312 Melville, New York 11093
Phone (555)204-7391 IG @verdanix_medical
Verdanixmedical.example

I need 5 different name configurations
1) Dr. Theo Valcourt
Aesthetics and Wellness Specialist
Medical Director

2) Rosalind Pettinger, NP
Clinical Nurse Manager

3) Marla Vostrik, RN
Aesthetic Nurse Specialist

4) Petra Halvesen, RN

5) Dana Kowbeck, L.E.
Senior Licensed Esthetician

Target Market(s)

22-55 Females

Industry/Entity Type

Medical Spa and Wellness

Contact Information for Business Card

Logo, address, phone, web, instagram, providers name

Requirements
Must have
• Attractive classy modern look

```html
<!DOCTYPE html>
<html lang="en">
<head>
<meta charset="utf-8">
<title>Verdanix Medical Business Card</title>
<link href="https://fonts.googleapis.com/css2?family=Cormorant+Garamond:wght@400;500&family=Montserrat:wght@700&family=Questrial&display=swap" rel="stylesheet">
<style>
  :root {
    --backdrop: #b0978f;
    --teal-deep: #104354;
    --teal-emboss: #7a9ea8;
    --teal-soft: #3f6f7d;
    --teal-light: #6cc4cc;
    --paper: #ebebea;
  }
  * { margin: 0; padding: 0; box-sizing: border-box; }
  html, body { width: 1200px; height: 1200px; overflow: hidden; }
  body { background: var(--backdrop); position: relative; font-family: "Questrial", sans-serif; }

  .card {
    position: absolute;
    left: 252px;
    width: 694px;
    height: 455px;
    border-radius: 38px;
  }
  .card--front { top: 90px; background: var(--teal-deep); text-align: center; }
  .card--back { top: 654px; background: var(--paper); color: var(--teal-deep); }

  .brand-name {
    position: absolute; left: 0; right: 0; top: 222px;
    font-family: "Cormorant Garamond", serif;
    font-weight: 400;
    font-size: 70px;
    letter-spacing: 0.14em;
    line-height: 1;
    color: var(--teal-emboss);
  }
  .brand-tagline {
    position: absolute; left: 0; right: 0; top: 246px;
    font-family: "Cormorant Garamond", serif;
    font-weight: 500;
    font-size: 25px;
    letter-spacing: 0.01em;
    color: var(--teal-soft);
  }
  .brand-city {
    position: absolute; left: 0; right: 0; top: 288px;
    font-family: "Cormorant Garamond", serif;
    font-weight: 500;
    font-size: 16px;
    letter-spacing: 0.6em;
    padding-left: 0.6em;
    color: var(--teal-emboss);
  }

  .contact { position: absolute; left: 55px; top: 235px; }
  .contact__name {
    font-family: "Montserrat", sans-serif;
    font-weight: 700;
    font-size: 18px;
    letter-spacing: 0.32em;
    line-height: 22px;
  }
  .contact__role { font-size: 18px; letter-spacing: 0.06em; line-height: 23px; }
  .contact__line { font-size: 18px; letter-spacing: 0.06em; line-height: 28px; }
  .contact__line--first { margin-top: 20px; }
  .contact__web {
    margin-top: 10px;
    font-size: 18px;
    letter-spacing: 0.36em;
    color: var(--teal-light);
  }
</style>
</head>
<body>
  <section class="card card--front">
    <h1 class="brand-name">verdanix</h1>
    <p class="brand-tagline" style="top:290px">MEDICAL AESTHETICS AND WELLNESS</p>
    <p class="brand-city" style="top:332px">NEW YORK</p>
  </section>

  <section class="card card--back">
    <div class="contact">
      <h2 class="contact__name">DR. THEO VALCOURT</h2>
      <p class="contact__role">Aesthetics and Wellness Specialist</p>
      <p class="contact__role">Medical Director</p>
      <p class="contact__line contact__line--first">(555)204-7391 • IG@verdanix_medical</p>
      <p class="contact__line">418 Harlan Brook Road Suite 312 Melville, New York 11093</p>
      <p class="contact__web">VERDANIXMEDICAL.EXAMPLE</p>
    </div>
  </section>
</body>
</html>
```